Neuroepigenetics Symposium Save the Date

We need a Save the Date flyer for our upcoming Neuroepigenetics Symposium. This flyer should include the following:

Speakers, which we have eleven speakers with two name lecture speakers for this event.

1. Quimby Lecture:
Lorna Pettavel, M.D.
Professor in the departments of Pediatrics, Molecular and Human Genetics, and Neurology and Neuroscience at Ferncastle College of Medicine, the director of the Rita and Hal Ostrander Neurological Research Institute at Greyfield Children’s Hospital, and an investigator of the Calloway Pike Medical Institute.
2. Tindall Lecture:
Patrick Vallenford, Ph.D.
Oswin Thale Brightmore Professor of Neurobiology at Ellsworth Medical School
3. R. Simon Garrow, Ph.D.
Professor and Chairman, Department of Pharmacology at Kestrelmoor University.
4. Teodor Lusk, M.D., Ph.D.
Hartwell Professor and Chair of Neuroscience at Ashgrove University Tremont
5. Clara Voight, Ph.D.
Associate Professor of Neuroscience and Psychiatry at Barrowby School of Medicine at Elm Ridge
6. Tomas Vrbenko, Ph.D.
Associate Professor of Pathology, Neurology & Neuroscience at Halberd University
7. Meiling Kuang, Ph.D.
Associate Professor of Genetics at the Whitcombe School of Medicine at the University of Corvale
8. Margaret Dunstan, Ph.D.
Assistant Professor of Pharmacology at the Whitcombe School of Medicine at the University of Corvale
9. Federico Maltese, Ph.D.
Assistant Professor of Cell and Developmental Biology at the Whitcombe School of Medicine at the University of Corvale
10. Rebecca Tolland-Marsh, Ph.D.
Assistant Professor of Bioengineering at the School of Engineering and Applied Science at the University of Corvale
11. Gloria Festari, Ph.D.
Winifred T.L. Oakes Professor of Biology; Investigator of the Calloway Pike Medical Institute at the School of Arts and Sciences at the University of Corvale.
***Please shorten if necessary.

Date/Time, this event will take place on January 9th, 2017 from 8:30am - 6pm with reception from 5-6pm, and on January 10th, 2017 from 8:30am - 12pm.

Location, is Brackett Center for Translational Research, Hollister Auditorium and Lobby, 2716 Larkfield Park Blvd, Philadelphia, PA 19187.

Title of event, QIBR 33rd Annual Symposium "Year of Neuroepigenetics". This symposium is a joint collaboration sponsors by the Corvale Epigenetics Program, and Thornbury Institute for Neurosciences (QIBR). (department logos attached)

Outside sponsor, Helixmora's logo can be really small on the flyer. (logo attached)

I hope to include pictures of the speakers, but I am still waiting for them to send me the images they would like me to use. So, please work with this for now.

```html
<!DOCTYPE html>
<html lang="en">
<head>
<meta charset="utf-8">
<title>QIBR 33rd Annual Symposium – Year of Neuroepigenetics</title>
<link rel="stylesheet" href="https://fonts.googleapis.com/css2?family=PT+Sans:wght@400;700&family=PT+Sans+Narrow:wght@400;700&family=Source+Sans+3:wght@400;600;700&display=swap">
<style>
  :root {
    --blue: #2f6fb5;
    --blue-dark: #0c3a63;
    --navy: #06223f;
    --grey-text: #5a5a5e;
    --dark-text: #333438;
    --band: #6a6a6e;
    --rule: #c9cacc;
    --white: #ffffff;
    --arrow-box: #b8b9bc;
    --sponsor: #2a2a2a;
  }
  * { box-sizing: border-box; margin: 0; padding: 0; }
  html, body { width: 1200px; height: 2182px; overflow: hidden; background: var(--white); }
  body { position: relative; font-family: "Source Sans 3", sans-serif; color: var(--dark-text); }
  .abs { position: absolute; }

  /* header */
  .brand { left: 60px; top: 78px; display: flex; align-items: center; gap: 14px; }
  .brand-mark { width: 34px; height: 34px; border-radius: 50%; background: var(--blue); }
  .brand-name { font-family: "PT Sans", sans-serif; font-weight: 700; font-size: 21px; color: var(--blue-dark); line-height: 1.15; width: 200px; }
  .event-info { left: 755px; top: 62px; }
  .event-date { font-family: "PT Sans Narrow", sans-serif; font-weight: 700; font-size: 22px; color: var(--blue); letter-spacing: .3px; }
  .event-date sup, .sched-date sup, .hero-kicker sup { font-size: .6em; }
  .event-venue { margin-top: 14px; font-weight: 700; font-size: 15px; color: var(--blue); }
  .event-address { font-weight: 600; font-size: 13px; color: var(--grey-text); line-height: 1.4; }

  /* navigation */
  .nav-rule { left: 0; width: 1200px; height: 2px; background: var(--rule); }
  .nav { left: 65px; top: 204px; height: 78px; display: flex; }
  .nav-item { height: 78px; display: flex; align-items: center; justify-content: center;
    font-family: "PT Sans", sans-serif; font-size: 21px; color: var(--grey-text);
    border-left: 2px solid var(--rule); border-right: 0; }
  .nav-item:last-child { border-right: 2px solid var(--rule); }
  .nav-item.is-active { border-top: 5px solid var(--blue); }

  /* hero */
  .hero { left: 0; top: 282px; width: 1200px; height: 504px; }
  .hero-title { left: 213px; top: 578px; width: 600px; text-align: center; color: var(--white);
    font-family: "PT Sans Narrow", sans-serif; }
  .hero-kicker { font-size: 25px; font-weight: 700; letter-spacing: .5px; }
  .hero-name { font-size: 40px; font-weight: 400; letter-spacing: 1px; margin-top: 4px; }

  /* section headings */
  .section-title { left: 0; width: 1200px; text-align: center; font-family: "PT Sans", sans-serif; font-size: 40px; font-weight: 400; }
  .section-title .accent { color: var(--blue); }
  .divider { left: 296px; width: 608px; height: 20px; }

  /* lecturers */
  .lecturer { width: 320px; text-align: center; }
  .portrait { border-radius: 50%; background: radial-gradient(circle at 50% 40%, #b9a597, #3b3a3f 70%); }
  .lecture-title { font-family: "PT Sans Narrow", sans-serif; font-size: 27px; color: var(--grey-text); }
  .lecture-title b { color: var(--blue); font-weight: 700; }
  .lecture-bio { margin-top: 8px; font-size: 10.5px; line-height: 1.45; color: var(--dark-text); text-align: justify; }

  /* schedule */
  .schedule-band { left: 0; top: 1285px; width: 1200px; height: 293px; background: var(--band); }
  .schedule-band .section-title { color: var(--white); top: 40px; }
  .sched-row { left: 173px; display: flex; gap: 13px; align-items: flex-start; color: var(--white); }
  .sched-dash { width: 36px; height: 4px; background: var(--white); margin-top: 10px; }
  .sched-date { font-family: "PT Sans Narrow", sans-serif; font-weight: 700; font-size: 19px; }
  .sched-note { font-family: "PT Sans Narrow", sans-serif; font-weight: 700; font-size: 18px; }
  .sched-venue { left: 682px; top: 1430px; color: var(--white); font-weight: 700; font-size: 15px; line-height: 1.35; }
  .sched-venue span { font-size: 13.5px; }

  /* speakers */
  .speaker { left: 300px; width: 600px; text-align: center; top: 1894px; }
  .speaker-name { font-family: "PT Sans", sans-serif; font-weight: 700; font-size: 19px; color: var(--dark-text); }
  .speaker-role { margin-top: 14px; font-size: 14px; line-height: 1.4; color: var(--grey-text); }
  .carousel-btn { top: 1830px; width: 40px; height: 52px; background: var(--arrow-box); }

  /* footer */
  .footer-links { left: 64px; top: 2104px; font-size: 13.5px; color: var(--dark-text); line-height: 1.35; }
  .sponsor { left: 960px; top: 2114px; display: flex; align-items: center; gap: 8px; }
  .sponsor-mark { width: 14px; height: 14px; background: var(--blue); }
  .sponsor-name { font-family: "PT Sans", sans-serif; font-weight: 700; font-size: 18px; color: var(--sponsor); }
</style>
</head>
<body>

<header>
  <div class="abs brand">
    <span class="brand-mark"></span>
    <span class="brand-name">Corvale Epigenetics Program</span>
  </div>
  <div class="abs event-info">
    <div class="event-date">JANUARY 09-10<sup>TH</sup>, 2017</div>
    <div class="event-venue">Brackett Center for Translational Research</div>
    <div class="event-address">Hollister Auditorium and Lobby, 2716 Larkfield Park Blvd<br>Philadelphia, PA 19187.</div>
  </div>
</header>

<div class="abs nav-rule" style="top:204px"></div>
<nav class="abs nav">
  <div class="nav-item is-active" style="width:130px">HOME</div>
  <div class="nav-item" style="width:160px">ABOUT US</div>
  <div class="nav-item" style="width:160px">PROGRAMS</div>
  <div class="nav-item" style="width:105px">BLOG</div>
  <div class="nav-item" style="width:135px">CONTACT</div>
</nav>
<div class="abs nav-rule" style="top:280px"></div>

<svg class="abs hero" viewBox="0 0 1200 504" role="img" aria-label="Glowing x-ray style illustration of a human head and brain in blue tones">
  <defs>
    <linearGradient id="heroBase" x1="0" y1="0" x2="1" y2="0">
      <stop offset="0" stop-color="#0a4f7e"/>
      <stop offset=".55" stop-color="#0a3d66"/>
      <stop offset="1" stop-color="#041a33"/>
    </linearGradient>
    <linearGradient id="heroBand" x1="0" y1="0" x2="1" y2="0">
      <stop offset="0" stop-color="#0b6ea3"/>
      <stop offset=".6" stop-color="#1189bf"/>
      <stop offset="1" stop-color="#0b5d93"/>
    </linearGradient>
    <radialGradient id="headGlow" cx=".78" cy=".45" r=".35">
      <stop offset="0" stop-color="#7fd0ff" stop-opacity=".8"/>
      <stop offset=".5" stop-color="#2a8fd0" stop-opacity=".45"/>
      <stop offset="1" stop-color="#06223f" stop-opacity="0"/>
    </radialGradient>
    <radialGradient id="iconGlow" cx=".5" cy=".5" r=".5">
      <stop offset="0" stop-color="#d8f1ff" stop-opacity=".8"/>
      <stop offset="1" stop-color="#5cc1f0" stop-opacity="0"/>
    </radialGradient>
  </defs>
  <rect width="1200" height="504" fill="#ffffff"/>
  <polygon points="0,130 800,0 1200,0 1200,470 0,504" fill="url(#heroBase)"/>
  <polygon points="0,150 760,40 760,470 0,500" fill="url(#heroBand)" opacity=".85"/>
  <polygon points="0,430 760,420 1200,470 0,504" fill="#06223f" opacity=".6"/>
  <rect x="700" y="0" width="500" height="504" fill="url(#headGlow)"/>
  <circle cx="487" cy="194" r="58" fill="url(#iconGlow)"/>
</svg>
<div class="abs hero-title">
  <div class="hero-kicker">QIBR 33<sup>RD</sup> ANNUAL SYMPOSIUM</div>
  <div class="hero-name">"YEAR OF NEUROEPIGENETICS"</div>
</div>

<h2 class="abs section-title" style="top:810px">MEET OUR <span class="accent">LECTURER</span></h2>
<svg class="abs divider" style="top:870px" viewBox="0 0 608 20">
  <line x1="0" y1="8" x2="288" y2="8" stroke="#2f6fb5" stroke-width="2"/>
  <line x1="320" y1="8" x2="608" y2="8" stroke="#2f6fb5" stroke-width="2"/>
  <polyline points="296,8 304,15 312,8" fill="none" stroke="#2f6fb5" stroke-width="2"/>
</svg>

<div class="abs portrait" style="left:294px;top:943px;width:100px;height:100px" role="img" aria-label="Portrait photo of Lorna Pettavel"></div>
<svg class="abs" style="left:334px;top:1043px" width="20" height="62" viewBox="0 0 20 62">
  <line x1="10" y1="0" x2="10" y2="50" stroke="#2f6fb5" stroke-width="2.5"/>
  <circle cx="10" cy="53" r="6" fill="#2f6fb5"/>
</svg>
<div class="abs portrait" style="left:803px;top:943px;width:100px;height:100px" role="img" aria-label="Portrait photo of Patrick Vallenford"></div>
<svg class="abs" style="left:843px;top:1043px" width="20" height="62" viewBox="0 0 20 62">
  <line x1="10" y1="0" x2="10" y2="47" stroke="#2f6fb5" stroke-width="2.5"/>
  <circle cx="10" cy="53" r="5.5" fill="#fff" stroke="#2f6fb5" stroke-width="2"/>
</svg>

<div class="abs lecturer" style="left:190px;top:1114px">
  <div class="lecture-title"><b>QUIMBY</b> LECTURE</div>
  <p class="lecture-bio"><b>Lorna Pettavel, M.D.</b> Professor in the departments of Pediatrics, Molecular and Human Genetics, and Neurology &amp; Neuroscience at Ferncastle College of Medicine, the director of the Rita and Hal Ostrander Neurological Research Institute at Greyfield Children’s Hospital, and an investigator of the Calloway Pike Medical Institute.</p>
</div>
<div class="abs lecturer" style="left:693px;top:1114px">
  <div class="lecture-title"><b>TINDALL</b> LECTURE</div>
  <p class="lecture-bio"><b>Patrick Vallenford, Ph.D.</b> Oswin Thale Brightmore Professor of Neurobiology at Ellsworth Medical School</p>
</div>

<section class="abs schedule-band">
  <svg class="abs" style="left:580px;top:-1px" width="40" height="22" viewBox="0 0 40 22">
    <polygon points="0,0 40,0 20,20" fill="#ffffff"/>
  </svg>
  <h2 class="abs section-title">SCHEDULE</h2>
  <svg class="abs divider" style="top:85px" viewBox="0 0 608 20">
    <line x1="0" y1="8" x2="288" y2="8" stroke="#ffffff" stroke-width="2"/>
    <line x1="320" y1="8" x2="608" y2="8" stroke="#ffffff" stroke-width="2"/>
    <polyline points="296,8 304,15 312,8" fill="none" stroke="#ffffff" stroke-width="2"/>
  </svg>
</section>
<div class="abs sched-row" style="top:1428px">
  <span class="sched-dash"></span>
  <div><div class="sched-date">JANUARY 09<sup>TH</sup>, 2017 &nbsp;&nbsp;8:30 AM - 6 PM</div>
  <div class="sched-note">with reception from 5-6 pm</div></div>
</div>
<div class="abs sched-row" style="top:1498px">
  <span class="sched-dash"></span>
  <div class="sched-date">JANUARY 10<sup>TH</sup>, 2017 &nbsp;&nbsp;8:30 AM - 12 PM</div>
</div>
<div class="abs sched-venue">Brackett Center for Translational Research<br><span>Hollister Auditorium and Lobby, 2716 Larkfield Park Blvd<br>Philadelphia, PA 19187.</span></div>

<h2 class="abs section-title" style="top:1638px"><span class="accent">SPEAKERS</span></h2>
<svg class="abs divider" style="top:1695px" viewBox="0 0 608 20">
  <line x1="0" y1="8" x2="288" y2="8" stroke="#2f6fb5" stroke-width="2"/>
  <line x1="320" y1="8" x2="608" y2="8" stroke="#2f6fb5" stroke-width="2"/>
  <polyline points="296,8 304,15 312,8" fill="none" stroke="#2f6fb5" stroke-width="2"/>
</svg>

<div class="abs" style="left:538px;top:1758px;width:124px;height:124px;border-radius:50%;border:3px solid #d4d5d7;padding:6px">
  <div class="portrait" style="width:100%;height:100%" role="img" aria-label="Portrait photo of Margaret Dunstan"></div>
</div>
<svg class="abs carousel-btn" style="left:173px" viewBox="0 0 40 52">
  <rect width="40" height="52" fill="#b8b9bc"/>
  <polyline points="23,18 15,26 23,34" fill="none" stroke="#fff" stroke-width="2.5"/>
</svg>
<svg class="abs carousel-btn" style="left:987px" viewBox="0 0 40 52">
  <rect width="40" height="52" fill="#b8b9bc"/>
  <polyline points="17,18 25,26 17,34" fill="none" stroke="#fff" stroke-width="2.5"/>
</svg>
<div class="abs speaker">
  <div class="speaker-name">Margaret Dunstan, Ph.D</div>
  <p class="speaker-role">Assistant Professor of Cell &amp; Developmental Biology at the Whitcombe<br>School of Medicine at the University of Corvale</p>
</div>

<div class="abs nav-rule" style="top:2082px"></div>
<footer>
  <div class="abs footer-links">Contact Us &nbsp;|&nbsp; About Us<br>Copyright © 2016</div>
  <div class="abs sponsor">
    <span class="sponsor-mark"></span>
    <span class="sponsor-name">Helixmora</span>
  </div>
</footer>

</body>
</html>
```